Physical Literacy company needs a web page designed...

We are a new company who provide physical education training to schools and deliver interventions to improve health and wellbeing, academic achievement through physical activity.

We need the website to have the following specification:
Creative design and production for 8 x page website for Kinetrova. Imagery and text as supplied by client. Fully responsive website design for multiple devices.
– 8 Main pages to website as per attached site plan – Twitter feed on home page
– Social Links - link to blog page
– Content management system for 2 pages
– Site Testing and Implementation
– Cookies policy and legal document templates if necessary

I am attaching a business plan PPT to give you a better idea of business. This should enable you to lift a lot of the content from the PPT also.

Target Market(s)

Physical Education - Schools
Families who wish to be more physically active

Industry/Entity Type

Education

Number of Pages Required

5+ page

Font styles to use
Sans Serif
Other font styles liked:
• Chalkboard

Colors
fbee3e
33a6d7
ec1f27
9bcb3c

Requirements
Must have
• *Home page
• *biog of company and four co-founders - who are well? What do we do? How do we do it? Contact details
• *Content management for two pages - blog page and case studies
• *Live twitter feed
• *links to youtube videos

```html
<!DOCTYPE html>
<html lang="en">
<head>
<meta charset="utf-8">
<title>Kinetrova – Home</title>
<link href="https://fonts.googleapis.com/css2?family=Dosis:wght@400;500;600;700&display=swap" rel="stylesheet">
<style>
:root{
  --purple:#8a6fcc;
  --purple-dark:#7a5fbd;
  --orange:#f9ad3f;
  --orange-dark:#e99a26;
  --red:#e8534f;
  --green:#9bc85a;
  --blue:#7bbad9;
  --text:#444;
  --white:#fff;
}
*{box-sizing:border-box;margin:0;padding:0}
html,body{width:1200px;height:1187px;overflow:hidden;background:var(--white);font-family:'Dosis',sans-serif;color:var(--text)}
.page{position:relative;width:1200px;height:1187px}

.top-strip{position:absolute;left:623px;top:0;width:577px;height:4px;display:flex}
.top-strip span{flex:1}

.brand{position:absolute;left:90px;top:38px;display:flex;align-items:center;gap:8px;font-size:28px;font-weight:700;color:var(--orange);letter-spacing:1px}
.brand i{display:block;width:14px;height:14px;border-radius:50%;background:var(--orange)}

.nav{position:absolute;left:640px;top:26px;display:flex}
.nav-item{width:98px;text-align:center;position:relative}
.nav-icon{width:44px;height:44px;border-radius:50%;margin:0 auto;display:flex;align-items:center;justify-content:center;border:2px solid var(--white);box-shadow:0 0 0 1px rgba(0,0,0,.12)}
.nav-label{display:block;margin-top:16px;font-size:15px;color:#555}
.nav-item.active .nav-label{color:var(--purple)}
.nav-item::after{content:"";position:absolute;right:0;top:62px;width:2px;height:12px;background:var(--sep)}

.hero{position:absolute;left:0;top:106px;width:1188px;height:448px;background:linear-gradient(90deg,#c98a5a 0%,#e0b070 30%,#f2c24a 45%,#e9e4dc 62%,#fafafa 80%,#fefefe 100%)}
.hero-brand{position:absolute;left:940px;top:482px;font-size:26px;font-weight:700;color:var(--orange);letter-spacing:1px}

.welcome{position:absolute;left:96px;top:585px;width:560px}
.welcome h1{font-size:30px;font-weight:600;color:var(--orange);margin-bottom:18px}
.welcome p{font-size:15px;line-height:26px}
.checks{list-style:none;margin-top:18px}
.checks li{font-size:15px;line-height:26.5px;display:flex;align-items:center;gap:10px}
.btn{display:inline-block;margin-top:26px;width:117px;height:39px;border-radius:5px;background:var(--orange);border:2px solid var(--orange-dark);color:var(--white);font-size:15px;font-weight:700;text-align:center;line-height:35px}

.team-photo{position:absolute;left:680px;top:645px;width:423px;height:244px;border-radius:50% 50% 12px 12px/30% 30% 12px 12px;background:radial-gradient(ellipse at 50% 60%,#d99a8a 0%,#e9c4b0 40%,#f6ece6 75%,#fff 100%)}

.stats{position:absolute;left:0;top:956px;width:1200px;height:214px;background:var(--purple)}
.stat{position:absolute;top:60px;width:236px;height:96px;border:1px solid rgba(0,0,0,.12);border-radius:4px;background:rgba(255,255,255,.04)}
.stat-icon{position:absolute;left:18px;top:19px;width:58px;height:58px;border-radius:50%;background:var(--purple-dark);display:flex;align-items:center;justify-content:center}
.stat-num{position:absolute;left:93px;top:14px;font-size:32px;font-weight:500;color:var(--white)}
.stat-label{position:absolute;left:93px;top:54px;font-size:13.5px;color:var(--white)}
</style>
</head>
<body>
<div class="page">
  <div class="top-strip">
    <span style="background:var(--purple)"></span><span style="background:var(--orange)"></span><span style="background:var(--red)"></span><span style="background:var(--green)"></span><span style="background:var(--blue)"></span><span style="background:var(--green)"></span>
  </div>

  <div class="brand"><i></i>KINETROVA</div>

  <nav class="nav">
    <div class="nav-item active" style="--sep:var(--purple)">
      <div class="nav-icon" style="background:var(--purple)"><svg width="16" height="16" viewBox="0 0 16 16"><path d="M8 2 1 8h2v6h4v-4h2v4h4V8h2z" fill="#fff"/></svg></div>
      <span class="nav-label">Home</span></div>
    <div class="nav-item" style="--sep:var(--orange)">
      <div class="nav-icon" style="background:var(--orange)"><svg width="16" height="16" viewBox="0 0 16 16"><path d="M5 2h9l-3 12H2z" fill="#fff"/></svg></div>
      <span class="nav-label">About Us</span></div>
    <div class="nav-item" style="--sep:var(--red)">
      <div class="nav-icon" style="background:var(--red)"><svg width="16" height="16" viewBox="0 0 16 16"><rect x="2" y="4" width="10" height="10" rx="1" fill="none" stroke="#fff" stroke-width="1.6"/><path d="M7 9l6-6 1.5 1.5-6 6H7z" fill="#fff"/></svg></div>
      <span class="nav-label">Our Packages</span></div>
    <div class="nav-item" style="--sep:var(--green)">
      <div class="nav-icon" style="background:var(--green)"><svg width="16" height="16" viewBox="0 0 16 16"><rect x="1.5" y="3" width="13" height="10" fill="none" stroke="#fff" stroke-width="1.6"/><path d="M3 12l4-4 3 3 2-2 2 3z" fill="#fff"/></svg></div>
      <span class="nav-label">Case Studies</span></div>
    <div class="nav-item" style="--sep:var(--blue)">
      <div class="nav-icon" style="background:var(--blue)"><svg width="16" height="16" viewBox="0 0 16 16"><path d="M2 14 11 5" stroke="#fff" stroke-width="2"/><path d="M12 1v3M14 3h-3M14 7v2M8 2h2" stroke="#fff" stroke-width="1.4"/></svg></div>
      <span class="nav-label">Contact Us</span></div>
  </nav>

  <div class="hero" role="img" aria-label="Child with paint-covered hands framing her eye beside colourful chalk alphabet letters"></div>
  <div class="hero-brand">KINETROVA</div>

  <section class="welcome">
    <h1>Welcome</h1>
    <p>Fusce pretium, est at aliquam semper, leo ante facilisis risus in feugiat ipsum augue pellent esque metu at luctus metus, non ornare lectus ac ipsum convallis fermentum ante a suscipit nunc. Etiam non scelerisque loren ornare dapibus libero sit amet facil sodales rutrum.</p>
    <ul class="checks">
      <li><svg width="14" height="12" viewBox="0 0 14 12"><path d="M1 6l4 4 8-9" fill="none" stroke="#555" stroke-width="2.6"/></svg>Donec tristique pellentesque duinon malesuada mi cursus nec amet quam justo</li>
      <li><svg width="14" height="12" viewBox="0 0 14 12"><path d="M1 6l4 4 8-9" fill="none" stroke="#555" stroke-width="2.6"/></svg>Ultricies ipsum dolor sit amet lisis massa velisectetur adipiscing elit oiels</li>
      <li><svg width="14" height="12" viewBox="0 0 14 12"><path d="M1 6l4 4 8-9" fill="none" stroke="#555" stroke-width="2.6"/></svg>Pellentesque fermentum sed sem nec port rutrum semper sed orem ipsum dolor sit</li>
    </ul>
    <a class="btn">Read more</a>
  </section>

  <div class="team-photo" role="img" aria-label="Group of mothers and toddlers sitting on the floor playing with building blocks"></div>

  <section class="stats">
    <div class="stat" style="left:113px">
      <div class="stat-icon"><svg width="30" height="24" viewBox="0 0 30 24"><path d="M15 2 1 8l14 6 14-6z" fill="#fff"/><path d="M7 11v6c4 4 12 4 16 0v-6l-8 3.5z" fill="#fff"/><path d="M27 9v8" stroke="#fff" stroke-width="1.6"/></svg></div>
      <div class="stat-num">2695</div><div class="stat-label">New Students</div></div>
    <div class="stat" style="left:359px">
      <div class="stat-icon"><svg width="28" height="26" viewBox="0 0 28 26"><path d="M8 2h12v7a6 6 0 0 1-12 0z" fill="#fff"/><path d="M8 4H3c0 5 3 7 5 7M20 4h5c0 5-3 7-5 7" fill="none" stroke="#fff" stroke-width="2"/><rect x="12" y="15" width="4" height="5" fill="#fff"/><rect x="8" y="20" width="12" height="4" fill="#fff"/></svg></div>
      <div class="stat-num">4568</div><div class="stat-label">Gold Medals</div></div>
    <div class="stat" style="left:604px">
      <div class="stat-icon"><svg width="28" height="26" viewBox="0 0 28 26"><path d="M9 2h17l-4 18H5z" fill="#fff"/><path d="M5 20 3 24h16l3-4" fill="none" stroke="#fff" stroke-width="2"/><path d="M11 7h10M10 11h10" stroke="var(--purple-dark)" stroke-width="1.6"/></svg></div>
      <div class="stat-num">8685</div><div class="stat-label">Total Courses</div></div>
    <div class="stat" style="left:851px">
      <div class="stat-icon"><svg width="26" height="28" viewBox="0 0 26 28"><path d="M9 2h8M10 2v9L2 25h22l-8-14V2" fill="#fff" stroke="#fff" stroke-width="2" stroke-linejoin="round"/></svg></div>
      <div class="stat-num">7856</div><div class="stat-label">Total Activities</div></div>
  </section>
</div>
</body>
</html>
```